Borrowdale Equity Business Card

Looking for a design for our business cards. Need to look corporate and outstanding. I have enclosed our logos for the company. Borrowdale equity is an investment firm for high level clients looking for advisory in their investments. White background or black is good. We will like to double sided options maybe at the back with just the logo of the firm.

Example of the info for the business card:

Marcus Heller
Managing Director

Panama Phone +507 391 4786
Switzerland Phone +41 43 917 2648
test@borrowdale-equity-example.com
www.borrowdale-equity-example.com

Industry/Entity Type

Investment

```html
<!DOCTYPE html>
<html lang="en">
<head>
<meta charset="utf-8">
<title>Borrowdale Equity Business Card</title>
<link rel="stylesheet" href="https://fonts.googleapis.com/css2?family=Montserrat:wght@400;600&family=Oswald:wght@500&display=swap">
<style>
  :root {
    --navy: #1f3f95;
    --navy-deep: #1a3480;
    --gold: #b48a2c;
    --white: #ffffff;
    --stage: #e4e5e9;
  }
  * { margin: 0; padding: 0; box-sizing: border-box; }
  html, body { width: 1200px; height: 974px; overflow: hidden; }
  body {
    background: var(--stage);
    font-family: "Montserrat", Arial, sans-serif;
    position: relative;
  }
  .card {
    position: absolute;
    left: 215px;
    width: 770px;
    height: 440px;
    background: var(--navy);
    overflow: hidden;
    box-shadow: 0 6px 18px rgba(0,0,0,0.18);
  }
  .card--back { top: 34px; }
  .card--front { top: 500px; }

  .panel {
    position: absolute;
    left: 16px;
    top: 16px;
    width: 738px;
    background: var(--white);
  }
  .card--back .panel {
    height: 334px;
    clip-path: polygon(0 0, 100% 0, 100% 100%, 46% 100%, 43.5% 94%, 41% 100%, 0 100%);
  }
  .card--front .panel {
    height: 204px;
    clip-path: polygon(0 0, 100% 0, 100% 100%, 19% 100%, 16.5% 90%, 14% 100%, 0 100%);
  }

  .brand {
    position: absolute;
    display: flex;
    align-items: center;
    gap: 14px;
    color: var(--navy);
    font-weight: 600;
    text-transform: uppercase;
    letter-spacing: 3px;
    white-space: nowrap;
  }
  .brand__square { background: var(--navy); flex: none; }
  .card--back .brand { left: 190px; top: 145px; font-size: 34px; }
  .card--back .brand__square { width: 34px; height: 34px; }
  .card--front .brand { left: 70px; top: 84px; font-size: 30px; }
  .card--front .brand__square { width: 30px; height: 30px; }

  .gold-band {
    position: absolute;
    background: var(--gold);
  }
  .card--back .gold-band { left: 440px; right: 16px; top: 360px; height: 40px; }
  .card--front .gold-band { left: 16px; right: 16px; top: 394px; height: 30px; }

  .website-line {
    position: absolute;
    left: 60px;
    top: 372px;
    color: var(--white);
    font-size: 14px;
    letter-spacing: 1px;
  }

  .person {
    position: absolute;
    left: 50px;
    top: 262px;
    color: var(--white);
  }
  .person__name {
    font-family: "Oswald", "Arial Narrow", sans-serif;
    font-weight: 500;
    font-size: 40px;
    line-height: 1;
    letter-spacing: 1px;
    text-transform: uppercase;
  }
  .person__role {
    margin-top: 8px;
    font-size: 13px;
    letter-spacing: 2px;
    text-transform: uppercase;
  }

  .divider {
    position: absolute;
    left: 336px;
    top: 240px;
    width: 2px;
    height: 130px;
    background: var(--white);
    opacity: 0.8;
  }

  .contacts {
    position: absolute;
    left: 362px;
    top: 234px;
    list-style: none;
    color: var(--white);
    font-size: 13.5px;
  }
  .contacts li {
    display: flex;
    align-items: center;
    gap: 12px;
    height: 27px;
    white-space: nowrap;
  }
  .contacts svg { width: 20px; height: 20px; flex: none; }
</style>
</head>
<body>

<section class="card card--back" aria-label="Card back">
  <div class="panel"></div>
  <div class="brand"><span class="brand__square"></span>Borrowdale Equity</div>
  <p class="website-line">www.borrowdale-equity-example.com</p>
  <div class="gold-band"></div>
</section>

<section class="card card--front" aria-label="Card front">
  <div class="panel"></div>
  <div class="brand"><span class="brand__square"></span>Borrowdale Equity</div>

  <div class="person">
    <p class="person__name">Marcus Heller</p>
    <p class="person__role">Managing Director</p>
  </div>

  <div class="divider"></div>

  <ul class="contacts">
    <li>
      <svg viewBox="0 0 20 20"><circle cx="10" cy="10" r="10" fill="var(--gold)"/><path d="M7 5.5l2 2-1 1.3c.6 1.3 1.6 2.3 2.9 2.9l1.3-1 2 2-1.2 1.5C9.8 14 6 10.2 5.8 6.7z" fill="var(--white)"/></svg>
      Panama +507 391 4786
    </li>
    <li>
      <svg viewBox="0 0 20 20"><circle cx="10" cy="10" r="10" fill="var(--gold)"/><path d="M7 5.5l2 2-1 1.3c.6 1.3 1.6 2.3 2.9 2.9l1.3-1 2 2-1.2 1.5C9.8 14 6 10.2 5.8 6.7z" fill="var(--white)"/></svg>
      Switzerland +41 43 917 2648
    </li>
    <li>
      <svg viewBox="0 0 20 20"><circle cx="10" cy="10" r="10" fill="var(--gold)"/><rect x="5" y="6.5" width="10" height="7" fill="none" stroke="var(--white)" stroke-width="1.3"/><path d="M5 6.8l5 4 5-4" fill="none" stroke="var(--white)" stroke-width="1.3"/></svg>
      test@borrowdale-equity-example.com
    </li>
    <li>
      <svg viewBox="0 0 20 20"><circle cx="10" cy="10" r="10" fill="var(--gold)"/><circle cx="10" cy="10" r="5" fill="none" stroke="var(--white)" stroke-width="1.2"/><path d="M5 10h10M10 5c-2.5 3-2.5 7 0 10M10 5c2.5 3 2.5 7 0 10" fill="none" stroke="var(--white)" stroke-width="1.1"/></svg>
      www.borrowdale-equity-example.com
    </li>
    <li>
      <svg viewBox="0 0 20 20"><circle cx="10" cy="10" r="10" fill="var(--gold)"/><path d="M10 15.5s-4-4.3-4-7a4 4 0 018 0c0 2.7-4 7-4 7z" fill="var(--white)"/><circle cx="10" cy="8.5" r="1.5" fill="var(--gold)"/></svg>
      41 Harbour View Road, Suite 3 West
    </li>
  </ul>

  <div class="gold-band"></div>
</section>

</body>
</html>
```